Spinning Wheel: Spin & Win

We are looking to design a large sticker cover for a spinning wheel (please see attached reference)

Wheel diameter: 120 cm (1.2meters)

Divided into 8 sections:
1- Free Meal
2- Tolvik Gift Card
3- Haircut or Blowdry
4- Tolvik Gift Card
5- Merchandise
6- Tolvik Gift Card
7- Meal voucher
8- Tolvik Gift Card

Text in the center:
Buy for 200 AED to Spin & Win!
(Spin & Win should be the most dominant visually)

Font: Something classy and elegant (maybe cursive but easily read)

Colors: Khaki - All shades of brown and dark brown (note: the wheel structure is made of wood that is dark brown)

Feel: Wood and Old Paper
Updates

Target Market(s)

Upper Class

Industry/Entity Type

Graphic Design

Font styles to use
Decorative
Script

Requirements
Should not have
• Flashy colors

```html
<!DOCTYPE html>
<html lang="en">
<head>
<meta charset="utf-8">
<title>Spin &amp; Win Wheel</title>
<link href="https://fonts.googleapis.com/css2?family=Almendra+Display&family=Almendra:wght@700&family=Libre+Baskerville:wght@700&display=swap" rel="stylesheet">
<style>
  :root {
    --bg: #ffffff;
    --orange-light: #f7941d;
    --orange-deep: #8f3e0a;
    --brown-light: #c26f34;
    --brown-dark: #7a4128;
    --brown-mid: #7b4a2a;
    --spoke: #c9a15a;
    --spoke-shadow: #4a2a1a;
    --rim: #b88a4a;
    --hub-light: #d67a2a;
    --hub-deep: #8a3a0c;
    --hub-ring: #a0552a;
    --label: #ffffff;
  }
  html, body {
    margin: 0;
    padding: 0;
    width: 1200px;
    height: 1200px;
    overflow: hidden;
    background: var(--bg);
  }
  .wheel {
    display: block;
    width: 1200px;
    height: 1200px;
  }
  .sector-orange { fill: url(#orangeSweep); }
  .sector-light { fill: var(--brown-light); }
  .sector-dark { fill: var(--brown-dark); }
  .sector-mid { fill: var(--brown-mid); }
  .spoke-line { stroke: var(--spoke); stroke-width: 3; }
  .spoke-shadow { fill: var(--spoke-shadow); opacity: 0.55; }
  .rim { fill: none; stroke: var(--rim); stroke-width: 3; }
  .prize-label {
    font-family: "Almendra Display", "Almendra", serif;
    font-size: 40px;
    fill: var(--label);
  }
  .hub { fill: url(#hubGlow); stroke: var(--hub-ring); stroke-width: 6; }
  .hub-small {
    font-family: "Libre Baskerville", Georgia, serif;
    font-weight: 700;
    font-size: 23px;
    fill: var(--label);
  }
  .hub-big {
    font-family: "Almendra", Georgia, serif;
    font-weight: 700;
    font-size: 62px;
    fill: var(--label);
  }
</style>
</head>
<body>
<svg class="wheel" viewBox="0 0 750 750" xmlns="http://www.w3.org/2000/svg">
  <defs>
    <linearGradient id="orangeSweep" x1="0" y1="0" x2="1" y2="1">
      <stop offset="0" style="stop-color: var(--orange-light)"/>
      <stop offset="0.45" style="stop-color: var(--orange-light)"/>
      <stop offset="1" style="stop-color: var(--orange-deep)"/>
    </linearGradient>
    <radialGradient id="hubGlow" cx="0.5" cy="0.35" r="0.7">
      <stop offset="0" style="stop-color: var(--hub-light)"/>
      <stop offset="1" style="stop-color: var(--hub-deep)"/>
    </radialGradient>
  </defs>

  <g class="sectors">
    <path class="sector-orange" d="M375,375 L375,3 A372,372 0 0 1 638,112 Z"/>
    <path class="sector-light" d="M375,375 L638,112 A372,372 0 0 1 747,375 Z"/>
    <path class="sector-dark" d="M375,375 L747,375 A372,372 0 0 1 638,638 Z"/>
    <path class="sector-light" d="M375,375 L638,638 A372,372 0 0 1 375,747 Z"/>
    <path class="sector-orange" d="M375,375 L375,747 A372,372 0 0 1 112,638 Z"/>
    <path class="sector-dark" d="M375,375 L112,638 A372,372 0 0 1 3,375 Z"/>
    <path class="sector-orange" d="M375,375 L3,375 A372,372 0 0 1 112,112 Z"/>
    <path class="sector-mid" d="M375,375 L112,112 A372,372 0 0 1 375,3 Z"/>
  </g>

  <g class="spokes" transform="translate(375 375)">
    <g transform="rotate(0)"><path class="spoke-shadow" d="M140,0 L300,-8 L372,0 L300,8 Z"/><line class="spoke-line" x1="0" y1="0" x2="372" y2="0"/></g>
    <g transform="rotate(45)"><path class="spoke-shadow" d="M140,0 L300,-8 L372,0 L300,8 Z"/><line class="spoke-line" x1="0" y1="0" x2="372" y2="0"/></g>
    <g transform="rotate(90)"><path class="spoke-shadow" d="M140,0 L300,-8 L372,0 L300,8 Z"/><line class="spoke-line" x1="0" y1="0" x2="372" y2="0"/></g>
    <g transform="rotate(135)"><path class="spoke-shadow" d="M140,0 L300,-8 L372,0 L300,8 Z"/><line class="spoke-line" x1="0" y1="0" x2="372" y2="0"/></g>
    <g transform="rotate(180)"><path class="spoke-shadow" d="M140,0 L300,-8 L372,0 L300,8 Z"/><line class="spoke-line" x1="0" y1="0" x2="372" y2="0"/></g>
    <g transform="rotate(225)"><path class="spoke-shadow" d="M140,0 L300,-8 L372,0 L300,8 Z"/><line class="spoke-line" x1="0" y1="0" x2="372" y2="0"/></g>
    <g transform="rotate(270)"><path class="spoke-shadow" d="M140,0 L300,-8 L372,0 L300,8 Z"/><line class="spoke-line" x1="0" y1="0" x2="372" y2="0"/></g>
    <g transform="rotate(315)"><path class="spoke-shadow" d="M140,0 L300,-8 L372,0 L300,8 Z"/><line class="spoke-line" x1="0" y1="0" x2="372" y2="0"/></g>
  </g>

  <circle class="rim" cx="375" cy="375" r="372"/>

  <g class="prize-labels" transform="translate(375 375)">
    <g transform="rotate(-67.5) translate(258 0) rotate(180)">
      <text class="prize-label" text-anchor="middle" dominant-baseline="central" textLength="195" lengthAdjust="spacingAndGlyphs">Free Meal</text>
    </g>
    <g transform="rotate(-22.5) translate(258 0) rotate(180)">
      <text class="prize-label" text-anchor="middle" dominant-baseline="central" textLength="220" lengthAdjust="spacingAndGlyphs">Tolvik Gift Card</text>
    </g>
    <g transform="rotate(22.5) translate(258 0)">
      <text class="prize-label" text-anchor="middle" dominant-baseline="central" textLength="225" lengthAdjust="spacingAndGlyphs">Haircut or Blowdry</text>
    </g>
    <g transform="rotate(67.5) translate(258 0) rotate(180)">
      <text class="prize-label" text-anchor="middle" dominant-baseline="central" textLength="220" lengthAdjust="spacingAndGlyphs">Tolvik Gift Card</text>
    </g>
    <g transform="rotate(112.5) translate(258 0) rotate(180)">
      <text class="prize-label" text-anchor="middle" dominant-baseline="central" textLength="190" lengthAdjust="spacingAndGlyphs">Merchandise</text>
    </g>
    <g transform="rotate(157.5) translate(258 0) rotate(180)">
      <text class="prize-label" text-anchor="middle" dominant-baseline="central" textLength="220" lengthAdjust="spacingAndGlyphs">Tolvik Gift Card</text>
    </g>
    <g transform="rotate(202.5) translate(258 0) rotate(180)">
      <text class="prize-label" text-anchor="middle" dominant-baseline="central" textLength="215" lengthAdjust="spacingAndGlyphs">Meal voucher</text>
    </g>
    <g transform="rotate(247.5) translate(258 0) rotate(180)">
      <text class="prize-label" text-anchor="middle" dominant-baseline="central" textLength="220" lengthAdjust="spacingAndGlyphs">Tolvik Gift Card</text>
    </g>
  </g>

  <g class="hub-group">
    <circle class="hub" cx="375" cy="375" r="133"/>
    <text class="hub-small" x="375" y="296" text-anchor="middle">Buy for</text>
    <text class="hub-small" x="375" y="333" text-anchor="middle">200 AED to</text>
    <text class="hub-big" x="375" y="395" text-anchor="middle">Spin &amp;</text>
    <text class="hub-big" x="375" y="460" text-anchor="middle">Win!</text>
  </g>
</svg>
</body>
</html>
```